Food Trade Show Advertisement

One full-page advertisement sent as a high-resolution .pdf file that is 11.125" w x 14.25" h

Details on the the wording and pictures will be provided
The to include:
Company logo, product photos (to be supplied), wording (to be supplied), Booth number (to be supplied)
Colors - hot pink
Attached is the guidelines for the advertisement

```html
<!DOCTYPE html>
<html lang="en">
<head>
<meta charset="UTF-8">
<title>Meadowvale – Sustainable Ingredients</title>
<link href="https://fonts.googleapis.com/css2?family=Poppins:wght@500;600;700;800&family=Oswald:wght@500&display=swap" rel="stylesheet">
<style>
  :root {
    --purple-deep: #68005e;
    --magenta: #b0107e;
    --hot-pink: #e6087a;
    --lime: #7cc41a;
    --brand-green: #2ee81c;
    --cyan: #00f5f5;
    --tick: #18d6f0;
    --white: #ffffff;
    --ink: #111111;
  }
  * { margin: 0; padding: 0; box-sizing: border-box; }
  html, body { width: 931px; height: 1200px; overflow: hidden; background: #ffffff; }
  .ad {
    position: relative;
    width: 931px; height: 1200px;
    background:
      radial-gradient(circle at 50% 58%, rgba(214,40,150,0.55), transparent 45%),
      linear-gradient(150deg, var(--purple-deep) 0%, #8a0a72 35%, var(--magenta) 65%, var(--hot-pink) 100%);
    font-family: "Poppins", sans-serif;
    color: var(--white);
    overflow: hidden;
  }
  .brand {
    position: absolute; top: 166px; left: 0; width: 100%;
    display: flex; justify-content: center; align-items: center; gap: 9px;
    font-weight: 800; font-size: 25px; letter-spacing: 3px; color: var(--brand-green);
  }
  .brand-dot { width: 15px; height: 15px; border-radius: 50%; background: var(--brand-green); }
  .headline {
    position: absolute; top: 228px; left: 0; width: 100%;
    text-align: center; font-weight: 700; font-size: 100px; line-height: 86px;
    letter-spacing: -1px; white-space: nowrap;
  }
  .tagline {
    position: absolute; top: 412px; left: 227px; width: 476px; height: 49px;
    background: var(--lime); border-radius: 9px;
    display: flex; align-items: center; justify-content: center;
    font-weight: 600; font-size: 35px; letter-spacing: 0.3px;
  }
  .produce-box {
    position: absolute; top: 483px; left: 69px; width: 793px; height: 102px;
    border: 2px solid var(--white); display: flex;
  }
  .produce-label {
    flex: 0 0 146px; border-right: 2px solid var(--white);
    padding: 8px 0 0 10px; overflow: hidden;
    font-family: "Oswald", sans-serif; font-weight: 500; font-size: 37px; line-height: 42px;
    text-transform: uppercase;
  }
  .produce-label span { display: block; transform: scaleX(0.84); transform-origin: left center; }
  .produce-label .accent { color: var(--lime); }
  .produce-list { padding: 14px 0 0 14px; }
  .products { display: flex; gap: 28px; list-style: none; font-weight: 700; font-size: 29px; line-height: 36px; }
  .products li { display: flex; align-items: center; gap: 7px; }
  .products svg { width: 19px; height: 19px; }
  .uses { font-weight: 500; font-size: 20.5px; margin-top: 2px; white-space: nowrap; }
  .band { position: absolute; top: 771px; left: 0; width: 100%; height: 222px; background: var(--cyan); }
  .product-photo {
    position: absolute; top: 662px; left: 92px; width: 750px; height: 358px;
    border-radius: 180px;
    background: radial-gradient(ellipse at 50% 50%, #f0d3a0 0%, #e3c090 40%, #c9b6a8 75%, #e8e4e4 100%);
  }
  .badge {
    position: absolute; top: 606px; left: 573px; width: 154px; height: 154px;
    border-radius: 50%; background: var(--lime); overflow: hidden;
    text-align: center;
  }
  .badge-number { font-family: "Oswald", sans-serif; font-weight: 500; font-size: 44px; line-height: 44px; margin-top: 30px; }
  .badge-unit { font-weight: 500; font-size: 16px; letter-spacing: 1.5px; line-height: 20px; }
  .badge-strip {
    margin: 3px auto 0; width: 150px; background: linear-gradient(90deg, var(--purple-deep), var(--hot-pink));
    font-family: "Oswald", sans-serif; font-weight: 500; font-size: 18px; letter-spacing: 2px; line-height: 28px;
  }
  .website {
    position: absolute; top: 1034px; left: 0; width: 100%;
    text-align: center; font-weight: 500; font-size: 34px; letter-spacing: 3.5px;
  }
  .website strong { font-weight: 700; }
  .booth {
    position: absolute; top: 1094px; left: 231px; width: 469px; height: 47px;
    display: flex; border-radius: 24px; overflow: hidden;
  }
  .booth-label {
    width: 344px; background: var(--lime);
    display: flex; align-items: center; justify-content: center;
    font-weight: 600; font-size: 30px;
  }
  .booth-number {
    flex: 1; background: var(--white); color: var(--ink);
    display: flex; align-items: center; padding-left: 18px;
    font-weight: 600; font-size: 30px;
  }
</style>
</head>
<body>
<main class="ad">
  <div class="brand"><span class="brand-dot"></span>MEADOWVALE</div>

  <h1 class="headline">SUSTAINABLE<br>INGREDIENTS</h1>
  <div class="tagline">DIRECT FROM THE FARM</div>

  <section class="produce-box">
    <div class="produce-label"><span>We</span><span class="accent">Produce</span></div>
    <div class="produce-list">
      <ul class="products">
        <li><svg viewBox="0 0 20 20"><circle cx="10" cy="10" r="10" fill="var(--tick)"/><path d="M5.5 10.2l3 3 6-6" fill="none" stroke="#5a0a6a" stroke-width="2.4" stroke-linecap="round" stroke-linejoin="round"/></svg>Protein</li>
        <li><svg viewBox="0 0 20 20"><circle cx="10" cy="10" r="10" fill="var(--tick)"/><path d="M5.5 10.2l3 3 6-6" fill="none" stroke="#5a0a6a" stroke-width="2.4" stroke-linecap="round" stroke-linejoin="round"/></svg>Fiber</li>
        <li><svg viewBox="0 0 20 20"><circle cx="10" cy="10" r="10" fill="var(--tick)"/><path d="M5.5 10.2l3 3 6-6" fill="none" stroke="#5a0a6a" stroke-width="2.4" stroke-linecap="round" stroke-linejoin="round"/></svg>Starch</li>
        <li><svg viewBox="0 0 20 20"><circle cx="10" cy="10" r="10" fill="var(--tick)"/><path d="M5.5 10.2l3 3 6-6" fill="none" stroke="#5a0a6a" stroke-width="2.4" stroke-linecap="round" stroke-linejoin="round"/></svg>Flour</li>
      </ul>
      <p class="uses">For Aquaculture, Feed, Pet Food and Human Consumption</p>
    </div>
  </section>

  <div class="band"></div>
  <div class="product-photo" role="img" aria-label="Three white bowls of green peas, soybeans and red lentils"></div>

  <div class="badge">
    <div class="badge-number">50,000</div>
    <div class="badge-unit">ACRES OF</div>
    <div class="badge-strip">EXPERIENCE</div>
  </div>

  <p class="website">www.<strong>meadowvalefoods</strong>.com</p>
  <div class="booth">
    <div class="booth-label">SEE YOU ON BOOTH</div>
    <div class="booth-number">106</div>
  </div>
</main>
</body>
</html>
```